Business Card Design Project

We have a logo, but would like to expand the use of it into a business card design. We are a B2B technology exchange platform for institutional investors to invest excess cash into short term assets matching their credit and pricing parameters. The assets are fractionalized and investors invest in portions.

Our customers are large, institutional, financial companies who are a bit traditional. We are high energy rebels with a cause...we are a disruptive technology and want to be viewed as a game changer but we need to present an image of trustworthiness and secure.

We are open not only to the image design but the material, die cut, etc. but want to stay in the traditional size of a business card.

We have other formats of the logo if needed. Our website is www.brambleharbor.com

I have posted a powerpoint template that we have been using.  This should not be considered the template we will use (after business cards we will have another project to incorporate business card design into powerpoint template) but just to give you a flavor of where we have been and have used in the past.

Target Market(s)

Institutional investors, asset managers, large fund institutions

Industry/Entity Type

Financial

Requirements
Must have
• Our logo
Traditional size
Nice to have
• unique use of logo, unique material, die cut, etc
Crisp, clean look
Use of both sides of card in a creative manner

```html
<!DOCTYPE html>
<html lang="en">
<head>
<meta charset="utf-8">
<title>Bramble Harbor — Business Card</title>
<link rel="stylesheet" href="https://fonts.googleapis.com/css2?family=Exo+2:wght@400;500&display=swap">
<style>
  :root {
    --stage: #5a5c5f;
    --orange: #f7931e;
    --black: #000000;
    --ink: #1a1a1a;
    --white: #ffffff;
    --silver: #c9cacc;
  }
  * { margin: 0; padding: 0; box-sizing: border-box; }
  html, body {
    width: 1200px;
    height: 800px;
    overflow: hidden;
    background: var(--stage);
    font-family: "Exo 2", Arial, sans-serif;
  }
  .stage {
    position: relative;
    width: 1200px;
    height: 800px;
  }
  .card {
    position: absolute;
    overflow: hidden;
    box-shadow: 0 6px 18px rgba(0,0,0,0.35);
  }
  /* Front side: contact details */
  .card-front {
    left: 60px;
    top: 294px;
    width: 630px;
    height: 420px;
    background: var(--orange);
    z-index: 1;
  }
  .name-band {
    position: absolute;
    left: 44px;
    right: 0;
    top: 272px;
    height: 40px;
    background: var(--black);
    display: flex;
    align-items: center;
    padding-left: 14px;
    font-size: 30px;
    font-weight: 500;
    letter-spacing: 0.5px;
    line-height: 1;
  }
  .name-first { color: var(--white); }
  .name-last { color: var(--orange); }
  .contact-list {
    position: absolute;
    left: 58px;
    top: 324px;
    list-style: none;
    color: var(--ink);
    font-size: 19px;
    line-height: 22px;
  }
  .contact-item {
    display: flex;
    align-items: center;
    gap: 10px;
  }
  .contact-icon { width: 16px; height: 16px; flex: none; }
  /* Back side: brand */
  .card-back {
    left: 508px;
    top: 88px;
    width: 684px;
    height: 416px;
    background: var(--black);
    z-index: 2;
  }
  .brand {
    position: absolute;
    left: 44px;
    top: 178px;
    display: flex;
    align-items: center;
    gap: 14px;
  }
  .brand-dot {
    width: 30px;
    height: 30px;
    border-radius: 50%;
    background: var(--orange);
  }
  .brand-name {
    color: var(--silver);
    font-size: 40px;
    font-weight: 500;
    letter-spacing: 1px;
    line-height: 1;
  }
</style>
</head>
<body>
  <main class="stage">
    <section class="card card-front" aria-label="Business card front">
      <div class="name-band">
        <span class="name-first">MARCUS</span><span class="name-last">HALLOWER</span>
      </div>
      <ul class="contact-list">
        <li class="contact-item">
          <svg class="contact-icon" viewBox="0 0 16 16" aria-hidden="true">
            <path d="M1 5 Q8 1 15 5 L13 7 L11 5.5 Q8 4.5 5 5.5 L3 7 Z" fill="#1a1a1a"/>
            <path d="M4 8 L12 8 L14 14 L2 14 Z" fill="#1a1a1a"/>
          </svg>
          <span>555.010.020</span>
        </li>
        <li class="contact-item">
          <svg class="contact-icon" viewBox="0 0 16 16" aria-hidden="true">
            <rect x="1" y="3" width="14" height="10" fill="#1a1a1a"/>
            <path d="M1.5 3.5 L8 9 L14.5 3.5" fill="none" stroke="#f7931e" stroke-width="1.3"/>
          </svg>
          <span>marcushallower@brambleharbor.com</span>
        </li>
      </ul>
    </section>

    <section class="card card-back" aria-label="Business card back">
      <div class="brand">
        <span class="brand-dot" aria-hidden="true"></span>
        <span class="brand-name">BRAMBLE HARBOR</span>
      </div>
    </section>
  </main>
</body>
</html>
```